'Bright Ledger Hidden Keys' Book Cover

I need a professional book cover design for my new upcoming book that shows people how to get a high credit score.

Here are my two websites:

https://www.moneywordbank-lexa.info
https://moneywordbank-lexa.com/

I am looking for a clean, professional design that pops (emotional touch) and separates from the other books that are on the market. Cover aspect ratio 1:4 for Pagewisp version and 1:5 for the paperback version. Yellow or blue are good colors - but not must. See the basic examples that I provided. File delivery format PDF.

Book Title: Bright Ledger Hidden Keys
Byline: The Quick Lift And Mend Manual for Stellar Borrowing

Currently on Brindlecart pre-order:
https://www.brindlecart.example/Bright-Ledger-Hidden-Keys-Stellar-ebook/dp/Q48MPLRT71

I am the author of 36 published books on Brindlecart. My author profile is here:
brindlecart.example/author/gideonvarly

Targeted audience: People that want to improve or repair their bad credit score.

Target Market(s)

People/consumers in the US that want to improve or repair their credit score.

Industry/Entity Type

Consumer

Font styles to use
Sans Serif

Colors

Designer to choose colors to be used in the design.

Requirements
Must have
• Author name, Title, byline, and graphic element(s).
Nice to have
• - 2020 edition logo / batch

```html
<!DOCTYPE html>
<html lang="en">
<head>
<meta charset="utf-8">
<title>Bright Ledger Hidden Keys – Book Cover</title>
<link rel="stylesheet" href="https://fonts.googleapis.com/css2?family=Oswald:wght@700&family=Open+Sans:wght@300;600;700&display=swap">
<style>
  :root {
    --page: #ffffff;
    --cover: #fbf7c4;
    --blue: #3aaae0;
    --blue-soft: #8cc8ec;
    --yellow: #f8cd12;
    --ink: #1c2a2f;
    --badge: #0d2e52;
  }
  * { margin: 0; padding: 0; box-sizing: border-box; }
  html, body {
    width: 1068px; height: 1200px; overflow: hidden;
    background: var(--page);
  }
  .canvas { position: relative; width: 1068px; height: 1200px; }
  .cover {
    position: absolute; left: 269px; top: 182px;
    width: 545px; height: 818px;
    background: var(--cover);
    overflow: hidden;
    font-family: "Open Sans", Arial, sans-serif;
    color: var(--ink);
  }
  .series-badge {
    position: absolute; left: 429px; top: 45px;
    width: 72px; height: 72px; border-radius: 50%;
    background: var(--badge);
  }
  .series-name {
    position: absolute; left: 45px; top: 124px; width: 460px;
    font-size: 13px; font-weight: 600;
    letter-spacing: 0.52em; white-space: nowrap;
    text-align: center;
  }
  .title {
    position: absolute; left: 45px; top: 155px;
    width: 458px; height: 150px;
  }
  .title text {
    font-family: "Oswald", Impact, sans-serif;
    font-weight: 700; fill: var(--blue);
  }
  .hero-art {
    position: absolute; left: 151px; top: 336px;
    width: 265px; height: 247px;
    border-radius: 10px;
    background: linear-gradient(170deg, var(--yellow) 0%, var(--yellow) 35%, var(--blue) 36%, var(--blue) 100%);
  }
  .divider {
    position: absolute; left: 191px; top: 630px;
    width: 161px; height: 2px; background: var(--yellow);
  }
  .subtitle {
    position: absolute; left: 0; top: 642px; width: 545px;
    text-align: center; font-size: 27px; line-height: 29px;
  }
  .subtitle .lead { display: block; font-weight: 300; }
  .subtitle .main { display: block; font-weight: 700; }
  .author {
    position: absolute; left: 0; top: 730px; width: 545px;
    text-align: center; font-size: 25px; font-weight: 600;
    letter-spacing: 0.04em;
  }
  .corner-art {
    position: absolute; left: 443px; top: 643px;
    width: 102px; height: 175px;
  }
</style>
</head>
<body>
<div class="canvas">
  <main class="cover">
    <div class="series-badge" aria-hidden="true"></div>
    <p class="series-name">VARLY FINANCIAL LITERACY PROGRAM</p>

    <svg class="title" viewBox="0 0 458 150" role="heading" aria-level="1" aria-label="Bright Ledger Hidden Keys">
      <text x="0" y="69" font-size="96" textLength="458" lengthAdjust="spacingAndGlyphs">BRIGHT LEDGER</text>
      <text x="0" y="145" font-size="79" textLength="458" lengthAdjust="spacingAndGlyphs">HIDDEN KEYS</text>
    </svg>

    <div class="hero-art" role="img" aria-label="Illustration of a blue credit card with yellow banknotes and a rising yellow arrow chart"></div>

    <div class="divider"></div>

    <p class="subtitle">
      <span class="lead">The Quick Lift and Mend</span>
      <span class="main">Manual for Stellar Borrowing</span>
    </p>

    <p class="author">GIDEON VARLY</p>

    <svg class="corner-art" viewBox="0 0 102 175" role="img" aria-label="Illustration of a tilted blue credit card at the corner">
      <polygon points="102,0 102,175 68,175 0,95 0,85 95,0" fill="var(--blue)"/>
    </svg>
  </main>
</div>
</body>
</html>
```